Old boys day 2025

HARTLEY FALCONS V BROOKVALE BULLS SUNDAY 10TH AUGUST
THIS IS A FREE EVENT FOR NEST MEMBERS
THE NEST WOULD LIKE TO WELCOME ALL PAST PLAYERS,
COACHES, COMMITTEE, SPONSORS & SUPPORTERS TO OUR
ANNUAL FALCON DAY OF CELEBRATION.
JOIN US IN THE PADDOCK FOR A GREAT DAY OF LEAGUE ACTION
WATCHING OUR CURRENT CROP OF FALCONS. YOU CAN PURCHASE A TICKET AND OR JOIN THE NEST @ WWW.HARTLEYNEST.COM.AU
IF YOU JOIN THE NEST PRIOR TO THE EVENT OLD BOYS DAY IS FREE OF CHARGE, YOU STILL NEED TO
PURCHASE/REGISTER A TICKET ON THE EVENTS PAGE SO WE KNOW YOU ARE ATTENDING.
WE WILL BE HONOURING 6 PREMIERSHIP WINNING TEAMS THIS YEAR: 1935 1ST GRADE (90 YEARS), 1980 RESERVE GRADE (45 YEARS), 1985 1ST GRADE (40 YEARS), 1985 U18'S (40 YEARS), 2005 1ST GRADE (20 YEARS) & 2015 1ST GRADE (10 YEARS)
IN THE 1ST GRADE GAME THE PLAYERS WILL BE WEARING REPLICA 1985 JERSEYS (attached) WITH THE 85 PLAYERS NAMES ON THE BACK, THE NEST WILL BE HOSTING A POST GAME FUNCTION AT THE WREN GATE INN WHERE THESE JERSEYS WILL BE AUCTIONED OFF TO RAISE MONEY.
PURCHASE YOUR TICKET AT WWW.HARTLEYNEST.COM.AU/EVENTS

Target Market(s)

ex players

Requirements
Must have
• I NEED A A4 FLYER DESIGN & A DESIGN THAT WILL SUIT SOCIAL MEDIA

```html
<!DOCTYPE html>
<html lang="en">
<head>
<meta charset="utf-8">
<title>Hartley Falcons Old Boys Day</title>
<link rel="stylesheet" href="https://fonts.googleapis.com/css2?family=Bebas+Neue&family=Kanit:ital,wght@0,300;0,400;1,800;1,900&family=Oswald:wght@300;600;700&family=Poppins:wght@400;500;600;700;800&display=swap">
<style>
  :root{
    --ink:#0b0b0b;
    --paper:#ffffff;
    --red:#c8102e;
    --red-soft:#f25a5a;
    --teal:#11b3a6;
    --teal-bright:#1fbcae;
    --grey-band:#5b5b5b;
    --panel:rgba(232,232,232,0.92);
    --note:#d2d2d2;
  }
  *{margin:0;padding:0;box-sizing:border-box}
  html,body{width:848px;height:1200px;overflow:hidden;background:var(--ink)}
  .flyer{position:relative;width:848px;height:1200px;overflow:hidden;background:var(--ink);font-family:"Poppins",sans-serif}

  .photo-field{position:absolute;left:0;top:615px;width:848px;height:440px;
    background:radial-gradient(ellipse at 70% 40%,#6e6e6e 0%,#3e3e3e 45%,#1c1c1c 100%)}
  .bottom-band{position:absolute;left:0;top:1048px;width:848px;height:152px;background:var(--grey-band)}
  .white-band{position:absolute;left:0;top:350px;width:848px;height:275px;display:block}

  .club-tab{position:absolute;left:42px;top:0;width:130px;height:174px;background:var(--paper);border-radius:0 0 65px 65px;
    display:flex;align-items:center;justify-content:center}
  .club-shield{width:92px;height:118px;border:4px solid var(--ink);border-radius:6px 6px 46px 46px;
    display:flex;align-items:center;justify-content:center;margin-top:6px}
  .club-shield span{font-family:"Kanit",sans-serif;font-weight:800;font-style:normal;font-size:18px;line-height:1.05;color:var(--ink);text-align:center}

  .title{position:absolute;left:204px;top:52px;font-family:"Kanit",sans-serif;font-style:italic;font-weight:900;
    font-size:52px;line-height:64px;letter-spacing:-1px;color:var(--paper);text-shadow:3px 4px 0 var(--red)}
  .title .away{color:var(--red-soft);text-shadow:3px 4px 0 #8c0f1c}

  .date{position:absolute;left:236px;top:196px;font-family:"Poppins",sans-serif;font-weight:700;font-size:27px;color:var(--teal-bright);letter-spacing:.3px}
  .welcome{position:absolute;left:264px;top:247px;width:400px;font-weight:600;font-size:16px;line-height:23px;color:var(--paper)}

  .free-badge{position:absolute;left:62px;top:188px;width:162px;height:162px}
  .free-text{position:absolute;left:90px;top:228px;width:110px;transform:rotate(-14deg);text-align:center;color:var(--paper);font-weight:800;line-height:1}
  .free-text .big{display:block;font-size:34px}
  .free-text .small{display:block;font-size:12px;margin-top:2px}
  .free-text .tiny{display:block;font-size:10px;margin-top:1px}

  .rival-tab{position:absolute;left:659px;top:240px;width:150px;height:122px;background:var(--paper);border-radius:75px 75px 0 0;
    display:flex;flex-direction:column;align-items:center;justify-content:center;gap:6px}
  .rival-tab span{font-family:"Poppins",sans-serif;font-weight:700;font-size:15px;line-height:1.1;color:var(--red);text-align:center}
  .rival-tab i{display:block;width:30px;height:30px;border-radius:50%;background:var(--red)}

  .jersey-disc{position:absolute;left:-21px;top:299px;width:328px;height:328px;border-radius:50%;background:var(--paper)}
  .jersey-art{position:absolute;left:56px;top:368px;width:184px;height:226px;border-radius:30px 30px 8px 8px;
    background:linear-gradient(160deg,#f4f4f4 0%,#dcdcdc 60%,#bdbdbd 100%)}
  .pointer{position:absolute;left:220px;top:526px;width:68px;height:46px}

  .join-copy{position:absolute;left:272px;top:392px;width:540px;text-align:center;transform:rotate(-2deg);
    font-family:"Bebas Neue",sans-serif;font-weight:400;font-size:36px;line-height:39px;color:var(--ink);text-transform:uppercase}
  .join-copy .venue{color:var(--red)}

  .auction-pill{position:absolute;left:294px;top:566px;width:496px;height:58px;background:var(--red-soft);border-radius:24px;
    transform:rotate(-2deg);display:flex;align-items:center;justify-content:center;text-align:center;
    color:var(--paper);font-size:13.5px;font-weight:500;line-height:19px;padding:0 20px}
  .auction-pill b{font-weight:800}

  .honour-head{position:absolute;left:0;top:660px;width:848px;text-align:center;font-family:"Oswald",sans-serif;font-weight:300;
    font-size:42px;line-height:46px;color:var(--paper)}
  .honour-head .accent{color:var(--teal);font-weight:700}

  .teams-panel{position:absolute;left:221px;top:771px;width:409px;height:227px;background:var(--panel);border-radius:14px}
  .team-badge{position:absolute;left:185px;top:795px;width:76px;height:96px;background:var(--paper);border:4px solid var(--ink);
    border-radius:4px 4px 38px 38px;display:flex;align-items:center;justify-content:center}
  .team-badge span{font-family:"Kanit",sans-serif;font-weight:400;font-size:10px;line-height:1.1;text-align:center;color:var(--ink)}
  .team-list{position:absolute;left:276px;top:787px;list-style:none}
  .team-list li{display:flex;align-items:center;height:33px;font-family:"Kanit",sans-serif;font-weight:300;font-size:20px;letter-spacing:1.6px;color:#1a1a1a}
  .team-list svg{width:12px;height:12px;margin-right:22px}

  .ticket-cta{position:absolute;left:147px;top:1030px;width:556px;height:83px;background:var(--teal);border-radius:42px;
    display:flex;flex-direction:column;align-items:center;justify-content:center;color:var(--paper);box-shadow:0 4px 10px rgba(0,0,0,.25)}
  .ticket-cta .lead{font-size:22px;font-weight:400;line-height:28px}
  .ticket-cta .url{font-size:23px;font-weight:800;line-height:30px}

  .fine-print{position:absolute;left:110px;top:1136px;width:628px;text-align:center;font-size:10.8px;line-height:14px;color:var(--note)}
</style>
</head>
<body>
<main class="flyer">

  <div class="photo-field" role="img" aria-label="Black and white photo of rugby league players in a tackle"></div>
  <div class="bottom-band"></div>

  <svg class="white-band" viewBox="0 0 848 275" preserveAspectRatio="none" aria-hidden="true">
    <polygon fill="#ffffff" points="0,12 40,8 90,14 150,6 220,12 300,8 360,14 430,4 520,10 600,6 680,12 760,6 848,10 848,262 790,268 700,260 620,266 540,258 460,266 380,260 300,268 220,260 140,266 60,258 0,264"/>
    <polygon fill="#0b0b0b" points="0,255 848,252 848,275 0,275"/>
  </svg>

  <div class="club-tab"><div class="club-shield"><span>THE<br>NEST</span></div></div>

  <h1 class="title">HARTLEY FALCONS<br>VS. <span class="away">BROOKVALE BULLS</span></h1>

  <p class="date">SUNDAY, 10TH AUGUST</p>
  <p class="welcome">THE NEST WOULD LIKE TO WELCOME ALL PAST PLAYERS, COACHES, COMMITTEE, SPONSORS &amp; SUPPORTERS TO OUR ANNUAL FALCON DAY OF CELEBRATION!</p>

  <div class="rival-tab"><i></i><span>BROOKVALE BULLS</span></div>

  <div class="jersey-disc"></div>
  <div class="jersey-art" role="img" aria-label="White replica 1985 jersey with black chevron collar"></div>
  <svg class="pointer" viewBox="0 0 68 46" aria-hidden="true">
    <path d="M2 4 C30 6 50 18 62 40" fill="none" stroke="#0b0b0b" stroke-width="1.6"/>
    <path d="M52 36 L62 41 L63 29" fill="none" stroke="#0b0b0b" stroke-width="1.6"/>
  </svg>

  <svg class="free-badge" viewBox="0 0 162 162" aria-hidden="true">
    <polygon fill="#11b3a6" points="81,0 92,12 107,5 113,20 129,19 129,35 144,40 138,55 151,64 141,77 151,90 138,100 144,114 129,120 129,136 113,135 107,150 92,143 81,156 70,143 55,150 49,135 33,136 33,120 18,114 24,100 11,90 21,77 11,64 24,55 18,40 33,35 33,19 49,20 55,5 70,12"/>
    <circle cx="81" cy="78" r="58" fill="none" stroke="#ffffff" stroke-width="2"/>
    <path d="M56 42 L74 38 M88 35 L106 31" stroke="#ffffff" stroke-width="2"/>
    <polygon fill="#ffffff" points="81,30 83,35 88,35 84,38 86,43 81,40 76,43 78,38 74,35 79,35"/>
  </svg>
  <div class="free-text"><span class="big">FREE</span><span class="small">ENTRY FOR</span><span class="tiny">NEST MEMBERS</span></div>

  <p class="join-copy">Join us in <span class="venue">The Paddock</span> for a great day of<br>league action watching our current crop<br>of Falcons. You can purchase a ticket and /<br>or join the Nest @ www.hartleynest.com.au</p>

  <p class="auction-pill"><span>REPLICA 1985 JERSEYS WILL BE ON AUCTION! JOIN OUR POST GAME FUNCTION AT THE WREN GATE INN - <b>DON'T MISS OUT!</b></span></p>

  <h2 class="honour-head">WE WILL BE HONOURING 6 PREMIERSHIP<br><span class="accent">WINNING TEAMS</span> THIS YEAR:</h2>

  <div class="teams-panel"></div>
  <div class="team-badge"><span>HARTLEY<br>FALCONS</span></div>
  <ul class="team-list">
    <li><svg viewBox="0 0 12 12"><path d="M1 1 L11 6 L1 11 L4 6 Z" fill="#111"/></svg>1935 1st grade (90 years)</li>
    <li><svg viewBox="0 0 12 12"><path d="M1 1 L11 6 L1 11 L4 6 Z" fill="#111"/></svg>1980 reserve grade (45 years)</li>
    <li><svg viewBox="0 0 12 12"><path d="M1 1 L11 6 L1 11 L4 6 Z" fill="#111"/></svg>1985 1st grade (40 years)</li>
    <li><svg viewBox="0 0 12 12"><path d="M1 1 L11 6 L1 11 L4 6 Z" fill="#111"/></svg>1985 u18's (40 years)</li>
    <li><svg viewBox="0 0 12 12"><path d="M1 1 L11 6 L1 11 L4 6 Z" fill="#111"/></svg>2005 1st grade (20 years)</li>
    <li><svg viewBox="0 0 12 12"><path d="M1 1 L11 6 L1 11 L4 6 Z" fill="#111"/></svg>2015 1st grade (10 years)</li>
  </ul>

  <div class="ticket-cta">
    <span class="lead">PURCHASE YOUR TICKET AT</span>
    <span class="url">WWW.HARTLEYNEST.COM.AU/EVENTS</span>
  </div>

  <p class="fine-print">*if you join the nest prior to the event, old boys day is free of charge, you still need to purchase/register a ticket on the events page so we know you are attending.</p>

</main>
</body>
</html>
```